Brindle Coffee, a new venture, serving our customers at functions and events, lovingly made coffee fro

www.brindlecoffee.com.au

Brindle Coffee Wordpress

The font type of our logo is: La Chatte à Maman (it can be downloaded in dafont.com)

Our trading name is Brindle Coffee. We have a passion for well made coffee and providing service with affection.

Our new logo design is being placed on the side and rear of our restored 1976 Kombi. I have attached our logo and a picture of our van. We would like to own the rights to all work on our site, with access to make additions and amendments as required with no restrictions.

We want our event business to grow through our branding of great service and lovingly made coffee.

We would like our WordPress design to be simple with a retro image that our 76 Kombi portrays as well as the hipster coffee culture of Melbourne.

To begin with we are thinking of 5 pages but are open to any suggestions you think would benefit our development. We would also like to have links to our new Facebook and Instagram pages on the bottom of each page.

Logo -Like us on Facebook
https://www.facebook.com/pages/Brindle-Coffee/9027316458810574

Logo -follow us on Instagram
Brindle_coffee

Home

Beautifully made coffee is a pleasure we should all enjoy at least once in our day.
Served from our restored 1976 Kombi we strive to provide you with an experience that will enhance your day. The care we show comes from years of training and experience as a Battista in several countries around the world.
We trust the joy of our lovingly made coffee and our retro style service will linger.
Serving great coffee at an event or function near you
Brindle Coffee.

About
Brindle coffee believes in good old fashion retro service and a high a quality product. We care that our customers receive a beautifully made coffee, chai or hot chocolate. We serve our patrons with a heartfelt smile, aiming to enhance their day.
We are fortunate enough to operate from our recently restored 1976 Kombi at functions and events around Melbourne.
You can follow us on Facebook and Instagram or book us for you special function via our contact page.
We look forward to wing able to serve you.
Brindle Coffee.

Contact Us - Safe and secure

To book us at your special function, please fill in your details below and we will respond to your query as soon as possible.

Name:

Company name:

Phone number:

Email address:

Question or comment: ( box )

Brindle Coffee
Melbourne, Victoria, Australia
Info@brindlecoffee.com.au
0461 925 274
Operating at your local function or event

Blog
Facebook and Instagram integration.

Links

We have a heartfelt passionate and eternal pursuit for exceeding expectations, providing a memorable experience. It follows that we align ourselves with organizations, business's and people who also strive for perfection in what they do, providing great services, products and customer care.

Feel free to contact some of our contacts below who we have found to be above and beyond.

The marrow group - equipment suppliers

http://www.brewtorrik.com.au

Kesh- barista consulting services

https://www.facebook.com/pages/Grand...Kesh/7719302846615098

Reedfinch Swimming Club

http://reedfinch.com.au/

Orvale Baseball Club

www.orvalebrambles.com.au/

Pelling Autos

http://www.pellingautos.com.au

Target Market(s)

Lovers of Coffee at events and functions. Customers wanting coffee catered for at their event of function

Industry/Entity Type

Cafe

Font styles to use
Other font styles liked:
• La Chatte à Maman

Requirements
Must have
• Our logo design
• 5 pages but are open to any suggestions you think would benefit our development. We would also like to have links to our new Facebook and Instagram pages on the bottom of each page.
Nice to have
• Your artistic flair and input

```html
<!DOCTYPE html>
<html lang="en">
<head>
<meta charset="utf-8">
<title>Brindle Coffee</title>
<link href="https://fonts.googleapis.com/css2?family=Lobster&family=Oswald:wght@400;500;600&family=Roboto:wght@400;500;700&display=swap" rel="stylesheet">
<style>
:root{
  --espresso:#2b1a10;
  --roast:#3a2416;
  --bark:#5a3520;
  --caramel:#e0a25a;
  --amber:#f0a04b;
  --rust:#b8331d;
  --cream:#fff8ef;
  --paper:#ffffff;
  --ink:#4a4a4a;
  --muted:#8a8a8a;
  --footer-link:#c9b7a6;
}
*{box-sizing:border-box;margin:0;padding:0}
html,body{width:710px;height:1200px;overflow:hidden}
body{position:relative;background:var(--paper);font-family:"Roboto",Arial,sans-serif;color:var(--ink)}
.abs{position:absolute}

/* top background */
.bean-backdrop{left:0;top:0;width:710px;height:430px;
  background:linear-gradient(180deg,#6b4a33 0%,#8a6a52 30%,#c9b8a8 62%,#ffffff 100%)}

/* utility bar */
.utility-bar{left:0;top:0;width:710px;height:30px;background:rgba(30,18,10,.85);color:#e8ddd2;font-size:10px}
.utility-links{left:66px;top:9px;letter-spacing:.2px}
.utility-links span{margin-right:14px}
.call-us{left:420px;top:8px;display:flex;align-items:center;gap:5px;font-size:11px}
.social-row{left:572px;top:8px;display:flex;gap:6px}
.social-dot{width:13px;height:13px;border-radius:50%;background:#c9b7a6}

/* header */
.brand{left:66px;top:36px;display:flex;align-items:center;gap:8px}
.brand-dot{width:22px;height:22px;border-radius:50%;background:var(--paper)}
.brand-name{font-family:"Lobster",cursive;font-size:30px;color:var(--paper);line-height:1}
.search-box{left:330px;top:54px;width:196px;height:22px;background:var(--paper);border:1px solid #ddd;font-size:10px;color:var(--muted);padding:5px 8px}
.search-box svg{position:absolute;right:6px;top:4px}
.cart{left:536px;top:54px;width:122px;height:22px;background:var(--roast);color:#fff;font-size:9px;display:flex;align-items:center;gap:6px;padding:0 8px}

/* nav */
.main-nav{left:66px;top:118px;width:592px;height:30px;background:linear-gradient(180deg,#7a4a28,#5a3520);display:flex;align-items:center}
.main-nav a{color:#fff;font-size:10px;font-weight:500;text-decoration:none;padding:0 14px;height:30px;line-height:30px}
.main-nav a.active{background:var(--roast)}

/* hero */
.hero{left:66px;top:148px;width:592px;height:232px;
  background:radial-gradient(circle at 72% 55%,#f4efe8 0 14%,#d9c7b2 22%,#6e4a30 45%,#3a2416 80%)}
.hero-title{left:92px;top:186px;font-family:"Oswald",sans-serif;font-weight:600;font-size:38px;line-height:44px;color:#fff;letter-spacing:.5px}
.hero-title em{font-style:normal;color:var(--rust)}
.hero-sub{left:92px;top:282px;font-family:"Oswald",sans-serif;font-size:14px;line-height:18px;color:#fff;letter-spacing:1px}

/* features */
.section-title{left:0;top:400px;width:710px;text-align:center;font-family:"Lobster",cursive;font-size:30px;color:var(--bark)}
.title-rule{top:424px;height:1px;width:220px;background:#d9cbbd}
.feature{top:476px;width:190px;text-align:center}
.feature-icon{width:80px;height:80px;border-radius:50%;background:var(--amber);margin:0 auto;display:flex;align-items:center;justify-content:center}
.feature h3{font-family:"Lobster",cursive;font-weight:400;font-size:28px;color:var(--espresso);margin-top:12px;line-height:1}
.feature h4{font-size:10px;font-weight:700;color:#333;margin-top:8px}
.feature p{font-size:9.5px;line-height:14px;color:var(--muted);margin-top:4px;padding:0 12px}

/* promo tiles */
.tile{top:705px;height:115px;display:flex;align-items:center;justify-content:center;text-align:center;color:#fff;font-family:"Oswald",sans-serif;font-size:15px;line-height:19px;letter-spacing:.5px}
.tile-iced{left:66px;width:178px;background:linear-gradient(135deg,#6e5a3c,#c9a46a 60%,#4a3a26)}
.tile-pursuit{left:260px;width:183px;background:linear-gradient(135deg,#2a1a10,#6b4528 50%,#d8c0a0)}
.tile-roasted{left:462px;width:184px;background:linear-gradient(135deg,#5a3520,#a8743e 55%,#3a2416)}

/* booking form */
.booking{left:66px;top:866px;width:580px;height:104px;background:var(--amber);padding:14px 16px}
.field-row{display:flex;gap:10px}
.field{flex:1;height:20px;background:#fff;font-size:9px;color:var(--muted);padding:5px 6px}
.field-message{margin-top:10px;height:38px;background:#fff}
.submit{left:297px;top:980px;width:118px;height:26px;background:var(--roast);color:#fff;font-family:"Lobster",cursive;font-size:17px;text-align:center;line-height:26px;border-radius:2px}

/* footer */
.site-footer{left:0;top:1022px;width:710px;height:178px;background:var(--espresso);color:var(--footer-link)}
.footer-brand{left:66px;top:1046px;display:flex;align-items:center;gap:5px}
.footer-brand .brand-name{font-size:15px}
.footer-brand .brand-dot{width:12px;height:12px}
.footer-col{top:1042px;font-size:9px;line-height:13px}
.footer-col h5{font-family:"Lobster",cursive;font-weight:400;font-size:15px;color:var(--amber);margin-bottom:4px}
.copyright{left:190px;top:1172px;font-size:8.5px;color:var(--footer-link)}
.footer-social{left:578px;top:1168px;display:flex;gap:6px}
.footer-social .social-dot{width:15px;height:15px;background:none;border:1px solid #8a7868}
</style>
</head>
<body>

<div class="abs bean-backdrop" role="img" aria-label="Photo of scattered roasted coffee beans fading into white"></div>

<div class="abs utility-bar">
  <div class="abs utility-links"><span>Sitemap</span><span>Contact Us</span></div>
  <div class="abs call-us">
    <svg width="10" height="10" viewBox="0 0 10 10"><path d="M2 1l2 2-1 1.2c.6 1.2 1.6 2.2 2.8 2.8L7 6l2 2-1.2 1.5C4.5 9.5.5 5.5.5 2.2z" fill="#e8ddd2"/></svg>
    <span>Call Us : 1300 482 719</span>
  </div>
  <div class="abs social-row"><span class="social-dot"></span><span class="social-dot"></span><span class="social-dot"></span><span class="social-dot"></span><span class="social-dot"></span></div>
</div>

<div class="abs brand"><span class="brand-dot"></span><span class="brand-name">Brindle Coffee</span></div>

<div class="abs search-box">Search
  <svg width="12" height="12" viewBox="0 0 12 12"><circle cx="5" cy="5" r="3.5" fill="none" stroke="#333" stroke-width="1.5"/><path d="M7.6 7.6L11 11" stroke="#333" stroke-width="1.6"/></svg>
</div>
<div class="abs cart">
  <svg width="12" height="11" viewBox="0 0 12 11"><path d="M0 1h2l1.5 6h7l1-4.5H3" fill="none" stroke="#fff" stroke-width="1.2"/><circle cx="4.5" cy="9.5" r="1" fill="#fff"/><circle cx="9.5" cy="9.5" r="1" fill="#fff"/></svg>
  <span>0 item(s) - $0.00</span>
</div>

<nav class="abs main-nav">
  <a class="active">HOME</a><a>BREWING GUIDES</a><a>SUBSCRIPTIONS</a><a>MERCHANDISE</a><a>BLOG</a><a>CONTACT US</a>
</nav>

<div class="abs hero" role="img" aria-label="Photo of a white cup of coffee on a saucer with cinnamon sticks and coffee beans"></div>
<div class="abs hero-title">COFFEE <em>OF THE</em><br>MONTH</div>
<div class="abs hero-sub">CLUB MEMBERSHIP &rsaquo;</div>

<div class="abs title-rule" style="left:66px"></div>
<div class="abs title-rule" style="left:424px"></div>
<h2 class="abs section-title" style="font-weight:400">Our Features</h2>

<div class="abs feature" style="left:55px">
  <div class="feature-icon">
    <svg width="34" height="26" viewBox="0 0 34 26"><circle cx="11" cy="7" r="5" fill="#fff"/><circle cx="23" cy="7" r="5" fill="#fff"/><path d="M2 24c0-7 4-10 9-10s9 3 9 10z M14 24c0-7 4-10 9-10s9 3 9 10z" fill="#fff"/></svg>
  </div>
  <h3>People</h3>
  <h4>wake your emotions with empore</h4>
  <p>Lorem ipsum dolor sit amet, consectetur adipiscing elit. Etiam posuere odio nec quam aliquet, varius consectetur neque metus.</p>
</div>

<div class="abs feature" style="left:248px">
  <div class="feature-icon">
    <svg width="28" height="30" viewBox="0 0 28 30"><rect x="3" y="2" width="22" height="26" rx="2" fill="none" stroke="#fff" stroke-width="2.5"/><path d="M9 12h8v6a4 4 0 01-8 0z M17 13h2a2 2 0 010 4h-2" fill="none" stroke="#fff" stroke-width="2"/></svg>
  </div>
  <h3>Coffee</h3>
  <h4>wake your emotions with empore</h4>
  <p>Lorem ipsum dolor sit amet, consectetur adipiscing elit. Etiam posuere odio nec quam aliquet, varius consectetur neque metus.</p>
</div>

<div class="abs feature" style="left:438px">
  <div class="feature-icon">
    <svg width="34" height="26" viewBox="0 0 34 26"><path d="M5 20a12 12 0 0124 0z" fill="#fff"/><rect x="2" y="21" width="30" height="3" rx="1.5" fill="#fff"/><circle cx="17" cy="6" r="2.5" fill="#fff"/></svg>
  </div>
  <h3>Dishes</h3>
  <h4>wake your emotions with empore</h4>
  <p>Lorem ipsum dolor sit amet, consectetur adipiscing elit. Etiam posuere odio nec quam aliquet, varius consectetur neque metus.</p>
</div>

<div class="abs tile tile-iced" role="img" aria-label="Photo of glasses of iced coffee on a table">ENJOYING GREAT<br>ICED COFFEE</div>
<div class="abs tile tile-pursuit" role="img" aria-label="Photo of a cup of black coffee with steam">THE PURSUIT OF THE<br>PERFECT COFFEE</div>
<div class="abs tile tile-roasted" role="img" aria-label="Photo of a sack of freshly roasted coffee beans">FRESHLY ROASTED<br>BEAN COFFEES</div>

<form class="abs booking">
  <div class="field-row">
    <div class="field">Name</div><div class="field">Company Name</div><div class="field">Email Address</div><div class="field">Phone</div>
  </div>
  <div class="field-message"></div>
</form>
<div class="abs submit">Submit Now</div>

<footer class="abs site-footer"></footer>
<div class="abs footer-brand"><span class="brand-dot"></span><span class="brand-name">Brindle Coffee</span></div>

<div class="abs footer-col" style="left:190px">
  <h5>Information</h5>
  <div>About Us</div><div>Delivery Information</div><div>Privacy Policy</div><div>Terms &amp; Conditions</div><div>Order History</div><div>Newsletter</div>
</div>
<div class="abs footer-col" style="left:303px">
  <h5>My Account</h5>
  <div>Contact Us</div><div>Returns</div><div>Site Map</div><div>My Account</div><div>Wish List</div><div>Affiliates</div>
</div>
<div class="abs footer-col" style="left:407px">
  <h5>Extras</h5>
  <div>Brands</div><div>Gift Vouchers</div><div>Affiliates</div><div>Specials</div><div>Newsletter</div><div>Returns</div>
</div>
<div class="abs footer-col" style="left:516px">
  <h5>Contact Us</h5>
  <div>Brindle Coffee</div><div>Melbourne, Victoria, Australia</div><div>Info@brindlecoffee.com.au</div><div>0461 925 274</div><div>Operating at your local function or event</div>
</div>

<div class="abs copyright">Copyright &copy; 2015 Brindle Coffee. All Rights Reserved.</div>
<div class="abs footer-social"><span class="social-dot"></span><span class="social-dot"></span></div>

</body>
</html>
```